Oil and Gas Letterhead Design Tweak

Simple letterhead information and design tweak.

Please note, we don't want to change the design or logo of the letterhead only the small changes mentioned below.

We need to change the company name up top to "Northvale Petrotek FZCO"

Also, we need to include in the footer the following information. I have attached an image of roughly how we would like to have it displayed in the footer.

Footer Details:

Northvale Petrotek FZCO,
Unit No. 2378, FZCO Trade Hub, level No. 1, K&P 7, Dubai, United Arab Emirates
Northvale Petrotek FZCO is registered as a free zone company under the rules & regulations of FZCO

Target Market(s)

O&G Market

Industry/Entity Type

Oil And Gas

Font styles to use
Sans Serif

Colors

Designer to choose colors to be used in the design.

Requirements
Must have
• Change the company name to Northvale Petrotek FZCO
• Include the footer on the bottom of the first and continuation page
Should not have
• Should not change the design or logo of the letterhead, only the specified changes mentioned above

```html
<!DOCTYPE html>
<html lang="en">
<head>
<meta charset="utf-8">
<title>Northvale Petrotek FZCO – Letterhead</title>
<link rel="stylesheet" href="https://fonts.googleapis.com/css2?family=Lato:wght@400;700&display=swap">
<style>
  :root {
    --brand-blue: #1557a8;
    --brand-red: #e3222b;
    --ink: #1d1d1d;
    --paper: #ffffff;
    --backdrop: #ffffff;
  }
  html, body {
    margin: 0;
    padding: 0;
    width: 1200px;
    height: 900px;
    overflow: hidden;
    background: var(--backdrop);
    font-family: "Lato", sans-serif;
    color: var(--ink);
  }
  .canvas {
    position: relative;
    width: 1200px;
    height: 900px;
  }
  .sheet {
    position: absolute;
    top: 181px;
    width: 383px;
    height: 538px;
    background: var(--paper);
    box-shadow: 0 1px 4px rgba(0,0,0,0.22);
    overflow: hidden;
  }
  .sheet--first { left: 209px; }
  .sheet--continuation { left: 607px; }
  .sheet svg.bands {
    position: absolute;
    left: 0;
    top: 0;
    width: 383px;
    height: 538px;
  }
  .band--blue { fill: var(--brand-blue); }
  .band--red { fill: var(--brand-red); }

  .masthead {
    position: absolute;
    top: 17px;
    left: 99px;
    display: flex;
    align-items: center;
    gap: 7px;
  }
  .masthead__dot {
    width: 10px;
    height: 10px;
    border-radius: 50%;
    background: var(--brand-blue);
  }
  .masthead__name {
    font-size: 11.4px;
    font-weight: 400;
    letter-spacing: 0.1px;
    color: var(--ink);
  }

  .footer {
    position: absolute;
    left: 28px;
    font-size: 6.6px;
    line-height: 10px;
    color: var(--ink);
  }
  .footer p { margin: 0; }
  .footer__name {
    font-weight: 700;
    font-size: 7.4px;
  }
  .sheet--first .footer { top: 489px; width: 345px; }
  .sheet--first .footer__name { color: var(--brand-blue); }
  .sheet--continuation .footer { top: 487px; width: 262px; }
  .sheet--continuation .footer__name { color: var(--brand-red); }

  .footer-mark {
    position: absolute;
    left: 283px;
    top: 497px;
    width: 44px;
    text-align: center;
    font-size: 4.2px;
    line-height: 5px;
    font-weight: 400;
    color: var(--ink);
  }
</style>
</head>
<body>
<main class="canvas">

  <section class="sheet sheet--first" aria-label="First page letterhead">
    <svg class="bands" viewBox="0 0 383 538" aria-hidden="true">
      <polygon class="band--blue" points="0,0 91,0 86,10 0,10"/>
      <polygon class="band--red" points="119,0 383,0 383,10 124,10"/>
      <polygon class="band--blue" points="281,528 295,528 290,538 275,538"/>
      <polygon class="band--red" points="300,528 312,528 316,538 295,538"/>
    </svg>
    <header class="masthead">
      <span class="masthead__dot"></span>
      <span class="masthead__name">NORTHVALE PETROTEK FZCO</span>
    </header>
    <footer class="footer">
      <p class="footer__name">Northvale Petrotek FZCO,</p>
      <p>Unit No. 2378 | FZCO Trade Hub | level No. 1, K&amp;P 7 | Dubai, | United Arab Emirates</p>
      <p>Northvale Petrotek FZCO is registered as a free zone company under the rules &amp; regulations of FZCO</p>
    </footer>
  </section>

  <section class="sheet sheet--continuation" aria-label="Continuation page letterhead">
    <svg class="bands" viewBox="0 0 383 538" aria-hidden="true">
      <polygon class="band--blue" points="277,0 312,0 306,14 284,14"/>
      <polygon class="band--red" points="318,0 339,0 331,14 312,14"/>
      <polygon class="band--blue" points="0,528 284,528 278,538 0,538"/>
      <polygon class="band--red" points="334,523 383,523 383,538 343,538"/>
    </svg>
    <footer class="footer">
      <p class="footer__name">Northvale Petrotek FZCO:</p>
      <p>Unit No. 2378 | FZCO Trade Hub | level No. 1, K&amp;P 7 | Dubai, | United Arab Emirates</p>
      <p>Northvale Petrotek FZCO is registered as a free zone company under the rules &amp; regulations of FZCO</p>
    </footer>
    <div class="footer-mark">NORTHVALE<br>PETROTEK FZCO</div>
  </section>

</main>
</body>
</html>
```